Cause bitches need love too!

I am creating an ad campaign. It will be a series of featured dogs in our shelter and they will contain a picture of the dog wich should be big enough to see on a yard sign and will change every week. I am placing the signs so that they lead you to the shelter. This is why I am also including the copy that says "you're almost there".

I have 4 tag lines:

1. Find unconditional Love.
2. She'll Love you furever!
3. He'll always listen.
4. Meet your new BFF

You're almost there 318 W Harrowgate Ln
Open 10 - 7/Tues-Sat

The dimensions for the sign are 24" wide and 18" high

Every week we will have a different picture of a different dog (hopefully last week's dog gets adopted). Anyhow, I am printing out yard signs, meaning that instead of printing 160 different signs it would be ideal just to replace the photo. So far the copy that is permanent is: "You're almost there. 318 W. Harrowgate Ln."

I could silhouette the image of the dog as well and super impose it on the sign, that's also a consideration, but ideally if I could have 4 tag lines I could print 40 signs of each and just replace the photo manually each week from my printer that would save costs.
Updates

Not enough designs to chose from and I edited the brief and committed to pay no matter what to increase the amount of designs as per your suggestions.

Target Market(s)

Animal lovers

Industry/Entity Type

Campaign

Font styles to use
Sans Serif

Colors

Designer to choose colors to be used in the design.

Requirements
Must have
• The dimensions for the sign are 24" wide and 18" high
Nice to have
• I want the signs to be hip, they should have a positive feel to them. You can alter the photos if you like. I am even open to new copy if you think something else works better.

```html
<!DOCTYPE html>
<html lang="en">
<head>
<meta charset="utf-8">
<title>You're Almost There – Shelter Yard Signs</title>
<link href="https://fonts.googleapis.com/css2?family=Oswald:wght@600&family=Archivo:wght@800&family=Kalam:wght@700&display=swap" rel="stylesheet">
<style>
  :root {
    --ink: #111111;
    --white: #ffffff;
    --photo-light: #c9c7c6;
    --photo-dark: #8a8785;

    --sun-bg: #fec501;
    --sun-frame: #ffdf1a;
    --sun-band: #e8141b;
    --sun-word: #ffe200;

    --rose-bg: #e84f55;
    --rose-frame: #f07830;
    --rose-band: #6b0e9a;
    --rose-word: #ee6d6d;

    --sea-bg: #0475b6;
    --sea-frame: #11927c;
    --sea-band: #fff200;
    --sea-word: #1c9bd0;

    --leaf-bg: #2da21c;
    --leaf-frame: #3fbf3a;
    --leaf-band: #9df5d5;
    --leaf-word: #2da21c;
  }
  * { box-sizing: border-box; margin: 0; padding: 0; }
  html, body { width: 1200px; height: 899px; overflow: hidden; background: var(--white); }

  .sign-set { position: relative; width: 1200px; height: 899px; }

  .sign {
    position: absolute;
    width: 567px; height: 431px;
    background: var(--bg);
    overflow: hidden;
  }
  .sign--sun  { left: 24px;  top: 16px;  --bg: var(--sun-bg);  --frame: var(--sun-frame);  --band: var(--sun-band);  --word: var(--sun-word); }
  .sign--rose { left: 607px; top: 16px;  --bg: var(--rose-bg); --frame: var(--rose-frame); --band: var(--rose-band); --word: var(--rose-word); }
  .sign--sea  { left: 24px;  top: 456px; --bg: var(--sea-bg);  --frame: var(--sea-frame);  --band: var(--sea-band);  --word: var(--sea-word); }
  .sign--leaf { left: 607px; top: 456px; --bg: var(--leaf-bg); --frame: var(--leaf-frame); --band: var(--leaf-band); --word: var(--leaf-word); }

  .photo-frame {
    position: absolute; left: 12px; top: 8px;
    width: 300px; height: 303px;
    background: var(--frame);
    padding: 11px;
  }
  .dog-photo {
    width: 100%; height: 100%;
    background: radial-gradient(ellipse at 55% 45%, var(--photo-light), var(--photo-dark));
  }

  .greeting-bubble { position: absolute; left: 307px; top: 4px; width: 96px; height: 74px; }
  .greeting-bubble text { font-family: "Kalam", sans-serif; font-weight: 700; font-size: 30px; fill: var(--ink); }

  .headline {
    position: absolute; left: 312px; top: 58px; width: 255px;
    font-family: "Oswald", sans-serif; font-weight: 600;
    text-transform: uppercase; color: var(--ink);
    text-align: right;
  }
  .headline__line {
    display: block; height: 52px;
    font-size: 60px; line-height: 52px;
    letter-spacing: -1px; padding-right: 12px;
  }
  .headline__band {
    display: block; height: 46px; margin: 3px 0;
    background: var(--band); color: var(--word);
    font-size: 44px; line-height: 46px; text-align: center;
  }

  .tagline {
    position: absolute; left: 326px; top: 240px; width: 226px;
    font-family: "Kalam", sans-serif; font-weight: 700;
    font-size: 21px; line-height: 22px;
    color: var(--band);
    transform: rotate(-6deg); transform-origin: center center;
    text-transform: uppercase; letter-spacing: 1px;
  }

  .address-bar {
    position: absolute; left: 104px; top: 330px;
    width: 463px; height: 56px;
    background: var(--white);
    display: flex; align-items: center;
    padding-left: 52px;
    font-family: "Archivo", sans-serif; font-weight: 800;
    font-size: 33px; letter-spacing: -0.5px; color: var(--ink);
    white-space: nowrap;
  }
  .map-pin { position: absolute; left: 98px; top: 320px; width: 46px; height: 68px; }
  .map-pin__body { fill: var(--band); stroke: var(--ink); stroke-width: 2.5; }
  .map-pin__dot { fill: var(--ink); }
</style>
</head>
<body>
<main class="sign-set">

  <section class="sign sign--sun">
    <div class="photo-frame"><div class="dog-photo" role="img" aria-label="Portrait photo of this week's featured shelter dog"></div></div>
    <svg class="greeting-bubble" viewBox="0 0 96 74"><path d="M48 4C22 4 4 18 4 34s14 28 30 30l-8 8 20-8c24 0 46-12 46-30S74 4 48 4z" fill="#fff" stroke="#111" stroke-width="3"/><text x="26" y="46">HI!</text></svg>
    <h2 class="headline"><span class="headline__line">You’re</span><span class="headline__band">Almost</span><span class="headline__line">There!</span></h2>
    <p class="tagline">Find unconditional love.</p>
    <div class="address-bar">318 W. Harrowgate Ln.</div>
    <svg class="map-pin" viewBox="0 0 46 68"><path class="map-pin__body" d="M23 3C12 3 3 12 3 23c0 14 20 42 20 42s20-28 20-42C43 12 34 3 23 3z"/><circle class="map-pin__dot" cx="23" cy="23" r="7"/></svg>
  </section>

  <section class="sign sign--rose">
    <div class="photo-frame"><div class="dog-photo" role="img" aria-label="Portrait photo of this week's featured shelter dog"></div></div>
    <svg class="greeting-bubble" viewBox="0 0 96 74"><path d="M48 4C22 4 4 18 4 34s14 28 30 30l-8 8 20-8c24 0 46-12 46-30S74 4 48 4z" fill="#fff" stroke="#111" stroke-width="3"/><text x="26" y="46">HI!</text></svg>
    <h2 class="headline"><span class="headline__line">You’re</span><span class="headline__band">Almost</span><span class="headline__line">There!</span></h2>
    <p class="tagline">She’ll<br>love you<br>furever!</p>
    <div class="address-bar">318 W. Harrowgate Ln.</div>
    <svg class="map-pin" viewBox="0 0 46 68"><path class="map-pin__body" d="M23 3C12 3 3 12 3 23c0 14 20 42 20 42s20-28 20-42C43 12 34 3 23 3z"/><circle class="map-pin__dot" cx="23" cy="23" r="7"/></svg>
  </section>

  <section class="sign sign--sea">
    <div class="photo-frame"><div class="dog-photo" role="img" aria-label="Portrait photo of this week's featured shelter dog"></div></div>
    <svg class="greeting-bubble" viewBox="0 0 96 74"><path d="M48 4C22 4 4 18 4 34s14 28 30 30l-8 8 20-8c24 0 46-12 46-30S74 4 48 4z" fill="#fff" stroke="#111" stroke-width="3"/><text x="26" y="46">HI!</text></svg>
    <h2 class="headline"><span class="headline__line">You’re</span><span class="headline__band">Almost</span><span class="headline__line">There!</span></h2>
    <p class="tagline">He’ll<br>always<br>listen.</p>
    <div class="address-bar">318 W. Harrowgate Ln.</div>
    <svg class="map-pin" viewBox="0 0 46 68"><path class="map-pin__body" d="M23 3C12 3 3 12 3 23c0 14 20 42 20 42s20-28 20-42C43 12 34 3 23 3z"/><circle class="map-pin__dot" cx="23" cy="23" r="7"/></svg>
  </section>

  <section class="sign sign--leaf">
    <div class="photo-frame"><div class="dog-photo" role="img" aria-label="Portrait photo of this week's featured shelter dog"></div></div>
    <svg class="greeting-bubble" viewBox="0 0 96 74"><path d="M48 4C22 4 4 18 4 34s14 28 30 30l-8 8 20-8c24 0 46-12 46-30S74 4 48 4z" fill="#fff" stroke="#111" stroke-width="3"/><text x="26" y="46">HI!</text></svg>
    <h2 class="headline"><span class="headline__line">You’re</span><span class="headline__band">Almost</span><span class="headline__line">There!</span></h2>
    <p class="tagline">Meet<br>your new<br>BFF</p>
    <div class="address-bar">318 W. Harrowgate Ln.</div>
    <svg class="map-pin" viewBox="0 0 46 68"><path class="map-pin__body" d="M23 3C12 3 3 12 3 23c0 14 20 42 20 42s20-28 20-42C43 12 34 3 23 3z"/><circle class="map-pin__dot" cx="23" cy="23" r="7"/></svg>
  </section>

</main>
</body>
</html>
```